Real Estate Investment Company Needs Business Card Design

TurnKeyMintHomes is a real estate investment company that primarily deals directly with homeowners looking to sell their homes in "as is" condition as quick as possible. We give this seller cash and close on their nightmare of a property in just a matter of days.

Our logo is attached - (please keep logo in tact, use as is)

Industry/Entity Type

Real Estate

Contact Information for Business Card

The design should invoke trust & professionalism. The person holding the card should feel rest assured that we are the right company to work with.

Font styles to use
Sans Serif

Requirements
Must have
• Card must include "Call us today for a fair offer on your property so you can move on with your life!"
Nice to have
• If possible, include this either on front or back (you can use your own formatting, below is just the text)
• "
• No Realtor Commissions
• No Repairs To Deal With
• No Closing Costs "

```html
<!DOCTYPE html>
<html lang="en">
<head>
<meta charset="utf-8">
<title>TurnKeyMintHomes Business Card</title>
<link href="https://fonts.googleapis.com/css2?family=Open+Sans:wght@400;600;700&display=swap" rel="stylesheet">
<style>
  :root {
    --page-bg: #d9dbdd;
    --card-black: #231f20;
    --card-white: #ffffff;
    --brand-blue: #1b8fe0;
    --brand-navy: #233a8f;
    --text-light: #ffffff;
    --text-muted: #e6e6e6;
    --divider: #8a8a8a;
  }
  * { margin: 0; padding: 0; box-sizing: border-box; }
  html, body { width: 1200px; height: 907px; overflow: hidden; }
  body {
    background: var(--page-bg);
    font-family: "Open Sans", Arial, sans-serif;
    position: relative;
  }
  .card {
    position: absolute;
    width: 540px;
    height: 310px;
    border-radius: 18px;
    overflow: hidden;
    box-shadow: 0 10px 24px rgba(0,0,0,0.25);
  }
  /* Back */
  .card-back { left: 50px; top: 150px; background: var(--card-black); }
  .back-brand {
    position: absolute; left: 40px; top: 0; width: 260px; height: 240px;
    display: flex; align-items: center; gap: 12px;
  }
  .back-brand-dot {
    width: 26px; height: 26px; border-radius: 50%; background: var(--card-white); flex: none;
  }
  .back-brand-name {
    color: var(--text-light); font-weight: 700; font-size: 22px; letter-spacing: 0.2px;
  }
  .back-divider {
    position: absolute; left: 318px; top: 60px; width: 1px; height: 120px; background: var(--divider);
  }
  .benefits {
    position: absolute; left: 338px; top: 75px; list-style: none;
    color: var(--text-light); font-size: 15px; line-height: 30px;
  }
  .benefits li::before {
    content: ""; display: inline-block; width: 8px; height: 8px;
    background: var(--card-white); margin-right: 8px; vertical-align: middle;
  }
  .back-tagline {
    position: absolute; left: 40px; right: 40px; bottom: 34px;
    text-align: center; color: var(--text-muted);
    font-size: 14px; line-height: 21px; font-weight: 600;
  }
  /* Front */
  .card-front { left: 610px; top: 450px; background: var(--card-black); }
  .front-shapes { position: absolute; inset: 0; width: 540px; height: 310px; }
  .front-brand {
    position: absolute; left: 26px; top: 28px; display: flex; align-items: center; gap: 10px;
  }
  .front-brand-dot { width: 22px; height: 22px; border-radius: 50%; background: var(--brand-blue); }
  .front-brand-name { color: var(--brand-blue); font-weight: 700; font-size: 26px; }
  .contact {
    position: absolute; right: 22px; top: 132px; list-style: none; text-align: right;
    color: var(--text-muted); font-size: 12px; line-height: 21px;
  }
  .contact li { display: flex; justify-content: flex-end; align-items: center; gap: 7px; }
  .contact svg { width: 10px; height: 10px; fill: var(--text-light); flex: none; }
  .contact .gap { margin-top: 10px; }
  .person {
    position: absolute; left: 26px; bottom: 20px; color: var(--text-light);
  }
  .person-name { font-weight: 700; font-size: 22px; line-height: 26px; }
  .person-title { font-size: 16px; line-height: 20px; margin-bottom: 12px; }
  .person-address { font-size: 13px; line-height: 19px; }
</style>
</head>
<body>
  <section class="card card-back">
    <div class="back-brand">
      <span class="back-brand-dot"></span>
      <span class="back-brand-name">TurnKeyMintHomes</span>
    </div>
    <div class="back-divider"></div>
    <ul class="benefits">
      <li>No Realtor Commisions</li>
      <li>No Repairs To Deal With</li>
      <li>No Closing Costs</li>
    </ul>
    <p class="back-tagline">Call us today for a fair offer on your property<br>so you can move on with your life!</p>
  </section>

  <section class="card card-front">
    <svg class="front-shapes" viewBox="0 0 540 310" preserveAspectRatio="none" aria-hidden="true">
      <path fill="var(--card-white)" d="M0,0 H540 V45 C420,105 240,140 0,150 Z"/>
      <path fill="var(--brand-navy)" d="M0,165 C180,152 310,115 390,55 C350,150 300,235 265,310 H0 Z"/>
      <path fill="var(--brand-blue)" d="M0,180 C180,168 300,130 378,72 C340,160 290,240 250,310 H0 Z"/>
    </svg>
    <div class="front-brand">
      <span class="front-brand-dot"></span>
      <span class="front-brand-name">TurnKeyMintHomes</span>
    </div>
    <ul class="contact">
      <li><svg viewBox="0 0 12 12"><path d="M2 1h3l1 3-2 1a7 7 0 0 0 3 3l1-2 3 1v3c-6 0-9-3-9-9z"/></svg>012-345-6789</li>
      <li><svg viewBox="0 0 12 12"><rect x="3" y="1" width="6" height="10" rx="1"/></svg>012-345-6789</li>
      <li class="gap"><svg viewBox="0 0 12 12"><path d="M1 3h10v7H1z"/></svg>info@turnkeyminthomes.com</li>
      <li><svg viewBox="0 0 12 12"><circle cx="6" cy="6" r="5"/></svg>www.turnkeyminthomes.com</li>
    </ul>
    <div class="person">
      <p class="person-name">Your Name</p>
      <p class="person-title">Title</p>
      <p class="person-address">Street Name, City Name<br>Zipcode-01234</p>
    </div>
  </section>
</body>
</html>
```